New Business Cards for Torvin Group

We need a new Business Card to compliment our new logo. We are a vibrant design, manufacture and install business providing recreation areas, public parks and Municipal spaces. We want business cards that are classy, modern and clean.

We have recently changed our logo, and are celebrating our 40th anniversary. We want business cards with a new modern design to reflect our status.

Target Market(s)

Customers

Contact Information for Business Card

We need all the details of our 3 offices as per the business card attached. Please disregard the old logo on the business card, the other three files show our new logo.

Requirements
Must have
• All info as per attached business card but with new logo.
Nice to have

```html
<!DOCTYPE html>
<html lang="en">
<head>
<meta charset="utf-8">
<title>Torvin Group – Business Card</title>
<link href="https://fonts.googleapis.com/css2?family=Roboto+Condensed:wght@400;700&display=swap" rel="stylesheet">
<style>
  :root {
    --stage: #e6e2dc;
    --card-black: #0c0c0c;
    --card-grey: #2a2a2a;
    --brand-red: #e0263c;
    --deep-red: #b3162a;
    --ink-white: #f2f2f2;
    --stripe-white: #d9d9d9;
  }
  * { margin: 0; padding: 0; box-sizing: border-box; }
  html, body {
    width: 1200px; height: 1023px; overflow: hidden;
    background: var(--stage);
    font-family: "Roboto Condensed", Arial, sans-serif;
  }
  .card {
    position: absolute; left: 100px; top: 226px;
    width: 1000px; height: 570px;
    border-radius: 6px; overflow: hidden;
    background: radial-gradient(ellipse at 40% 20%, var(--card-grey) 0%, var(--card-black) 60%);
    box-shadow: 0 14px 40px rgba(0,0,0,.35);
    color: var(--ink-white);
  }
  .brand {
    position: absolute; left: 60px; top: 120px;
    display: flex; align-items: center; gap: 22px;
  }
  .brand-dot {
    width: 120px; height: 120px; border-radius: 50%;
    background: var(--brand-red);
  }
  .brand-name {
    font-weight: 700; font-size: 56px; line-height: 1;
    text-transform: uppercase; color: var(--ink-white);
  }
  .contact {
    position: absolute; right: 50px; top: 40px; text-align: right;
  }
  .contact-name {
    color: var(--brand-red); font-size: 38px; font-weight: 400; letter-spacing: .5px;
  }
  .contact-role { font-size: 22px; margin: 2px 34px 10px 0; }
  .contact-line {
    display: flex; justify-content: flex-end; align-items: center; gap: 10px;
    font-size: 22px; line-height: 1.35;
  }
  .contact-line svg { width: 22px; height: 22px; flex: none; }
  .divider {
    position: absolute; left: 60px; right: 50px; top: 268px;
    height: 2px; background: var(--brand-red);
  }
  .offices {
    position: absolute; left: 60px; top: 290px;
    display: flex; gap: 70px;
  }
  .office h2 {
    color: var(--brand-red); font-weight: 400; font-size: 30px; margin-bottom: 4px;
  }
  .office p { font-size: 20px; line-height: 1.3; }
  .office .gap { margin-top: 18px; }
  .office .label { color: var(--brand-red); }
  .edge { position: absolute; left: 0; bottom: 0; width: 1000px; height: 90px; }
</style>
</head>
<body>
  <section class="card">
    <div class="brand">
      <span class="brand-dot"></span>
      <span class="brand-name">Torvin Group</span>
    </div>

    <div class="contact">
      <h1 class="contact-name">KARIM DALLOUL</h1>
      <p class="contact-role">Managing Partner</p>
      <p class="contact-line">+971 (0)50 384 7192
        <svg viewBox="0 0 24 24"><path fill="#e0263c" d="M6.6 10.8a15 15 0 0 0 6.6 6.6l2.2-2.2a1 1 0 0 1 1-.25 11.4 11.4 0 0 0 3.6.6 1 1 0 0 1 1 1V20a1 1 0 0 1-1 1A17 17 0 0 1 3 4a1 1 0 0 1 1-1h3.5a1 1 0 0 1 1 1c0 1.25.2 2.45.6 3.6a1 1 0 0 1-.25 1z"/></svg></p>
      <p class="contact-line">karim@torvingroup.com
        <svg viewBox="0 0 24 24"><rect x="3" y="5" width="18" height="14" rx="2" fill="#e0263c"/><path d="M4 7l8 6 8-6" stroke="#0c0c0c" stroke-width="2" fill="none"/></svg></p>
      <p class="contact-line">www.torvingroup.com
        <svg viewBox="0 0 24 24"><circle cx="12" cy="12" r="9" fill="none" stroke="#e0263c" stroke-width="2"/><path d="M3 12h18M12 3c3 3 3 15 0 18M12 3c-3 3-3 15 0 18" stroke="#e0263c" stroke-width="1.6" fill="none"/></svg></p>
    </div>

    <div class="divider"></div>

    <div class="offices">
      <div class="office">
        <h2>Head Office</h2>
        <p>P.O. Box:</p>
        <p>31842 Abu Dhabi, U.A.E.</p>
        <p class="gap"><span class="label">P :</span> +971 (0)2 4471236</p>
        <p><span class="label">F :</span> +971 (0)2 4471237</p>
        <p><span class="label">E :</span> sales@torvingroup.com</p>
      </div>
      <div class="office">
        <h2>Dubai Office</h2>
        <p>P.O. Box:</p>
        <p>407216 Dubai, U.A.E.</p>
        <p class="gap"><span class="label">P :</span> +971 (0)4 4528403</p>
        <p><span class="label">F :</span> +971 (0)4 4528404</p>
        <p><span class="label">E :</span> sales@torvingroup.com</p>
      </div>
      <div class="office">
        <h2>Qatar Office</h2>
        <p>P.O. Box:</p>
        <p>15273 Doha, Qatar</p>
        <p class="gap"><span class="label">P :</span> +974 44710382</p>
        <p><span class="label">F :</span> +974 44735916</p>
        <p><span class="label">E :</span> sales@torvingroup.com</p>
      </div>
    </div>

    <svg class="edge" viewBox="0 0 1000 90" preserveAspectRatio="none" aria-hidden="true">
      <path d="M0 62 H600 C635 62 640 34 680 34 H1000" fill="none" stroke="var(--stripe-white)" stroke-width="5"/>
      <path d="M0 70 H610 C648 70 652 42 692 42 H1000 V90 H0 Z" fill="var(--brand-red)"/>
      <path d="M0 84 H1000 V90 H0 Z" fill="var(--deep-red)"/>
    </svg>
  </section>
</body>
</html>
```